Wolkenfeld - a property developer - Website design

Hi all!
Exciting new project for you! :)
We are looking for some creative/modern designs to best represent us as a company.
Please have a look at the following link: huhu.wolkenfeld.eu to get an idea about who we are and what we do.
The 'Main Page' of the HP should be neatly arranged, easy to navigate, contain several pictures (changing every 10 seconds or so) that should reflect that we are property developers.
The navigation points ('About us', 'Projects' 'Investment', 'Contact Us', 'Legal Notice') should be included in the Design (again under every navigation point, pictures may be added - that reflect our profession and/or the subsection)
What we will need at the end of the day is a fully functional site - i.e: a site that is designed and programmed with backend/wordpress, to allow us to make changes anytime we feel like it.
Further questions?! Don't hesitate to contact me! Thanks :)
Target Market(s)
Real Estate Development/Building sector
Industry/Entity Type
Real Estate Development
Number of Pages Required
5+ page
Look and feel

```html
<!DOCTYPE html>
<html lang="en">
<head>
<meta charset="utf-8">
<title>Wolkenfeld – Property Developer</title>
<link href="https://fonts.googleapis.com/css2?family=Open+Sans:wght@400;600;700&display=swap" rel="stylesheet">
<style>
:root{
  --teal:#17a58b;
  --navy:#1c2b3c;
  --footer:#163450;
  --text:#6d7378;
  --light:#f4f5f6;
  --line:#e4e6e8;
  --white:#ffffff;
}
*{box-sizing:border-box;margin:0;padding:0}
html,body{width:1200px;height:3495px;overflow:hidden}
body{position:relative;font-family:"Open Sans",Arial,sans-serif;color:var(--text);background:var(--white)}
.abs{position:absolute}
a{color:var(--teal);text-decoration:none}

/* header / hero */
.hero{left:0;top:0;width:1200px;height:580px;background:linear-gradient(160deg,#3d4a55 0%,#6f7d86 35%,#a9b6bd 55%,#56636c 80%,#2c363e 100%)}
.navbar{left:0;top:0;width:1200px;height:100px;background:rgba(20,30,40,.55)}
.brand{left:116px;top:30px;display:flex;align-items:center;gap:12px;color:var(--white);font-weight:700;font-size:22px;letter-spacing:.5px}
.brand-mark{width:38px;height:38px;border-radius:50%;background:var(--white)}
.nav{left:455px;top:38px;display:flex;gap:34px;align-items:center}
.nav span{color:var(--white);font-size:13px;font-weight:600;letter-spacing:.6px}
.nav .active{border-bottom:2px solid var(--teal);padding-bottom:4px}
.search{width:30px;height:30px;border-radius:50%;background:var(--teal);display:flex;align-items:center;justify-content:center}
.thumb{top:474px;width:205px;height:186px;border:4px solid var(--white);box-shadow:0 4px 14px rgba(0,0,0,.2)}

/* section headings */
.heading{left:0;width:1200px;text-align:center;font-size:27px;font-weight:700;color:var(--navy)}
.heading em{font-style:normal;color:var(--teal)}
.sub{left:380px;width:440px;text-align:center;font-size:12px;line-height:18px}

.photo{width:272px;height:240px}
.projects{left:0;top:1405px;width:1200px;height:650px;background:var(--light);border-top:1px solid var(--line)}
.proj-img{width:172px;height:172px;border-radius:50%;border:5px solid var(--white);box-shadow:0 3px 10px rgba(0,0,0,.15)}
.badge{width:40px;height:40px;border-radius:50%;background:var(--teal);color:var(--white);font-weight:700;font-size:15px;display:flex;align-items:center;justify-content:center;border:3px solid var(--white)}
.proj-text{width:220px}
.proj-text h3{font-size:19px;color:var(--navy);font-weight:700;margin-bottom:10px}
.proj-text p{font-size:12px;line-height:18px;margin-bottom:8px}
.proj-text a{font-size:12px;font-weight:600}

.invest-img{left:415px;top:2221px;width:303px;height:322px;background:linear-gradient(180deg,#8fb3cf 0%,#c9d7e2 40%,#7c8d99 75%,#3f4d57 100%)}
.play{left:546px;top:2362px;width:40px;height:40px;border-radius:50%;background:var(--white);display:flex;align-items:center;justify-content:center}
.invest-text{left:750px;top:2243px;width:280px;font-size:13px;line-height:21px}
.invest-text p{margin-bottom:18px}

.divider{left:0;width:1200px;height:1px;background:var(--line)}
.legal-col{top:2835px;font-size:12px;line-height:18px}
.legal-col h4{font-size:13px;color:var(--navy);font-weight:700;margin-bottom:6px}
.legal-col h4.teal{color:var(--teal)}
.legal-col .gap{margin-top:12px}

.map{left:0;top:3126px;width:1200px;height:291px;background:linear-gradient(135deg,#ecebe6 0%,#e2e0d8 50%,#eceae3 100%)}
.footer{left:0;top:3417px;width:1200px;height:78px;background:var(--footer);color:#c7d2dc;font-size:12px}
.footer .copy{left:175px;top:30px}
.socials{left:935px;top:24px;display:flex;gap:10px}
.socials span{width:30px;height:30px;border-radius:50%;background:rgba(255,255,255,.18)}
</style>
</head>
<body>

<header class="abs hero" role="img" aria-label="Modern office interior with glass walls and lounge chairs"></header>
<div class="abs navbar"></div>
<div class="abs brand"><span class="brand-mark"></span>WOLKENFELD</div>
<nav class="abs nav">
  <span class="active">HOME</span><span>ABOUT US</span><span>PROJECTS</span><span>INVESTMENT</span><span>CONTACT US</span><span>LEGAL NOTICE</span>
  <span class="search"><svg width="14" height="14" viewBox="0 0 14 14"><circle cx="6" cy="6" r="4.2" fill="none" stroke="#fff" stroke-width="1.8"/><line x1="9" y1="9" x2="13" y2="13" stroke="#fff" stroke-width="1.8"/></svg></span>
</nav>
<div class="abs thumb" style="left:175px;background:linear-gradient(180deg,#cfd9e2,#8a7a6c)" role="img" aria-label="Residential apartment building"></div>
<div class="abs thumb" style="left:396px;background:linear-gradient(180deg,#f1f1ef,#bfc3c4)" role="img" aria-label="Bright living room interior"></div>
<div class="abs thumb" style="left:617px;background:linear-gradient(180deg,#d9dde1,#55595d)" role="img" aria-label="Modern cubic house exterior"></div>
<div class="abs thumb" style="left:833px;background:linear-gradient(180deg,#eae7e2,#7f7468)" role="img" aria-label="Contemporary kitchen and dining area"></div>

<!-- quality section -->
<h2 class="abs heading" style="top:722px">Quality, skills and experience: <em>everything under one roof.</em></h2>
<p class="abs sub" style="top:770px">Wolkenfeld is a combination of potent companies pursuing a common goal: the realization of modern, sustainable housing projects for highest demands in Nordstadt.</p>
<div class="abs photo" style="left:175px;top:846px;background:linear-gradient(180deg,#8fb9de,#e8ecef 60%,#9aa57a)" role="img" aria-label="White modern villa under blue sky"></div>
<div class="abs photo" style="left:464px;top:846px;background:linear-gradient(180deg,#a9c4dc,#d8d3c4 55%,#6e8a54)" role="img" aria-label="Terraced family homes with gardens"></div>
<div class="abs photo" style="left:753px;top:846px;background:linear-gradient(180deg,#c4d7e6,#c9cdd0 55%,#7d8b63)" role="img" aria-label="Multi-storey residential complex"></div>
<div class="abs photo" style="left:175px;top:1103px;background:linear-gradient(180deg,#b7cde0,#d5d0c5 55%,#6f8a4e)" role="img" aria-label="Classic detached house with lawn"></div>
<div class="abs photo" style="left:464px;top:1103px;background:linear-gradient(180deg,#7fb2e0,#f2f2ee 55%,#4fa3c2)" role="img" aria-label="White villa with palm trees and pool"></div>
<div class="abs photo" style="left:753px;top:1103px;background:linear-gradient(180deg,#8fb0d4,#e3e1dc 55%,#8c8f7d)" role="img" aria-label="Apartment block with balconies"></div>

<!-- projects -->
<section class="abs projects"></section>
<h2 class="abs heading" style="top:1467px">Our <em>Projects</em></h2>
<p class="abs sub" style="top:1512px">Wolkenfeld is a combination of potent companies pursuing a common goal: the realization of modern, sustainable housing projects for highest demands in Nordstadt.</p>

<div class="abs proj-img" style="left:175px;top:1592px;background:linear-gradient(180deg,#c9d6e0,#8d6f58)" role="img" aria-label="Townhouse project"></div>
<div class="abs badge" style="left:170px;top:1592px">1</div>
<div class="abs proj-text" style="left:369px;top:1600px"><h3>Ahornweg</h3><p>We place the highest value on location, architecture and features of our projects, and offer our clients more.</p><a>View group »</a></div>

<div class="abs proj-img" style="left:621px;top:1592px;background:linear-gradient(180deg,#d8dde1,#6f6660)" role="img" aria-label="Row house project"></div>
<div class="abs badge" style="left:616px;top:1592px">2</div>
<div class="abs proj-text" style="left:804px;top:1600px"><h3>Ahornweg</h3><p>We place the highest value on location, architecture and features of our projects, and offer our clients more.</p><a>View group »</a></div>

<div class="abs proj-img" style="left:175px;top:1825px;background:linear-gradient(180deg,#a9c5de,#6d7f56)" role="img" aria-label="Family house project"></div>
<div class="abs badge" style="left:170px;top:1825px">3</div>
<div class="abs proj-text" style="left:369px;top:1833px"><h3>Family house</h3><p>We place the highest value on location, architecture and features of our projects, and offer our clients more.</p><a>View group »</a></div>

<div class="abs proj-img" style="left:621px;top:1825px;background:linear-gradient(180deg,#b9c2c9,#4b4f52)" role="img" aria-label="Apartment building project"></div>
<div class="abs badge" style="left:616px;top:1825px">4</div>
<div class="abs proj-text" style="left:804px;top:1833px"><h3>Appartements</h3><p>We place the highest value on location, architecture and features of our projects, and offer our clients more.</p><a>View group »</a></div>

<!-- investment -->
<h2 class="abs heading" style="top:2112px">Build up on a <em>safe investment.</em></h2>
<p class="abs sub" style="top:2158px">Wolkenfeld is a combination of potent companies pursuing a common goal: the realization of modern, sustainable housing projects for highest demands in Nordstadt.</p>
<div class="abs invest-img" role="img" aria-label="High-rise residential tower in the city"></div>
<div class="abs play"><svg width="14" height="14" viewBox="0 0 14 14"><path d="M4 2 L11 7 L4 12 Z" fill="#1c2b3c"/></svg></div>
<div class="abs invest-text">
  <p>Invest now in the future of housing. Starting with an investment from 300.000 Euro you can participate in an exclusive roof extension at a development project by Wolkenfeld. Benefit from uniquely successful projects with high returns and security in the best regions.</p>
  <p>Do you want to know more?<br>Simply contact us by email to <a>investment@wolkenfeld.eu</a></p>
</div>

<!-- legal -->
<div class="abs divider" style="top:2640px"></div>
<h2 class="abs heading" style="top:2714px">Legal <em>Notice</em></h2>
<p class="abs sub" style="top:2760px">Wolkenfeld is a combination of potent companies pursuing a common goal: the realization of modern, sustainable housing projects for highest demands in Nordstadt.</p>

<div class="abs legal-col" style="left:175px;width:200px">
  <h4>WOLKENFELD.AT<br>WOLKENFELD.EU</h4>
  <p class="gap">Lindengasse 12/4<br>1070 Nordstadt</p>
  <p class="gap">Phone: <a>+43 1 000 1 234</a><br>Fax: +43 1 000 1 235<br>email: <a>office@wolkenfeld.at</a></p>
</div>
<div class="abs legal-col" style="left:408px;width:300px">
  <h4>Nordlicht Property GmbH</h4>
  <p>VAT-ID-Nr.: ATU 00000000<br>Register number of the company: 000000 x<br>Companies court: Firmengericht Nordstadt</p>
  <h4 class="teal gap">Aurelia Real Estate GmbH</h4>
  <p>VAT-ID-Nr.: ATU 00000001<br>Register number of the company: 000001 x<br>Companies court: Firmengericht Nordstadt</p>
</div>
<div class="abs legal-col" style="left:745px;width:290px">
  <h4>K&amp;M Liegenschaftsverwertung GmbH</h4>
  <p>VAT-ID-Nr.: ATU 00000002<br>Register number of the company: 000002 x<br>Companies court: Firmengericht Nordstadt</p>
  <h4 class="teal gap">Handelskammer Ost</h4>
  <p>Member of the chamber of commerce<br>Section: real estate and property trade</p>
  <p class="gap">Trade licence and supervisory body:<br>Stadtamt Nordstadt</p>
</div>

<!-- map and footer -->
<div class="abs map" role="img" aria-label="Street map showing the office location"></div>
<footer class="abs footer">
  <span class="abs copy">© Copyright 2016 | wolkenfeld.at &amp; wolkenfeld.eu | All rights reserved</span>
  <div class="abs socials"><span></span><span></span><span></span><span></span><span></span></div>
</footer>

</body>
</html>
```